Give my personal webpage more appeal!

I need my CV website improved - drmeganholt.com.au.
I am using the template KESTREL from pagecraftly. i would like to keep the already existing theme but am open to suggestions.
Please focus on imagery, colour scheme, and textures to enhance the appeal and look of the page.
The content is there, but now I need a designer to improve the look of my page.
I need styling, royalty-free unique modern images to make the page professional, personal and friendly.
I work in healthcare, so I'm a people person.
I teach professionals and I treat a lot of families.

Target Market(s)

Parents, Professional Healthcare providers

Number of Pages Required

1 page

Font styles to use
Serif
Sans Serif

Requirements
Must have
• My face - image at the top, all the information already contained in it.
• Links to the websites I manage such as my blog.
• One Page website.
• All the information it already contains with the ability to have more.
• Ideally, we would keep the same format for the page although I'm happy to expand column and change the page's structure with in the theme template KESTREL.
Nice to have
• The current KESTREL template. I would like to keep the already existing theme but am open to suggestions.
Should not have
• Multiple pages.

```html
<!DOCTYPE html>
<html lang="en">
<head>
<meta charset="utf-8">
<title>Dr Megan Holt – Chiropractor</title>
<link href="https://fonts.googleapis.com/css2?family=Raleway:wght@300;400;500;600;700&family=Open+Sans:wght@400;600;700&family=Merriweather:ital@1&family=Oswald:wght@400;500&display=swap" rel="stylesheet">
<style>
:root{
  --orange:#f0a30a;
  --orange-dark:#d98f00;
  --grey:#858585;
  --grey-dark:#6e6e6e;
  --text:#555;
  --cream:#fdf6e8;
  --white:#fff;
}
*{box-sizing:border-box;margin:0;padding:0}
html,body{width:1200px;height:3947px;overflow:hidden}
body{font-family:"Open Sans",Arial,sans-serif;color:var(--text);background:#fff;font-size:14px}
.wrap{width:1045px;margin:0 auto;position:relative;height:100%}
section,header,footer,nav{position:relative;width:1200px}
.btn{display:inline-flex;height:52px;background:var(--orange);color:#fff;font-family:"Raleway",sans-serif;font-weight:600;font-size:19px;align-items:center}
.btn span{padding:0 18px}
.btn i{width:40px;height:52px;background:var(--grey);display:flex;align-items:center;justify-content:center}
.h-section{font-family:"Raleway",sans-serif;font-weight:400;color:var(--orange);font-size:40px;text-align:center;letter-spacing:1px}

/* top bar */
.topbar{height:40px;border-bottom:1px solid #eee}
.social{position:absolute;top:6px;left:0;display:flex;gap:8px}
.social b{width:28px;height:28px;border:2px solid var(--orange);border-radius:50%;display:block}
.top-contact{position:absolute;right:0;top:9px;display:flex;gap:26px;font-size:14px;color:#666;align-items:center}
.top-contact span{display:flex;gap:8px;align-items:center}

/* header */
.masthead{height:118px}
.call{position:absolute;left:0;top:28px;display:flex;gap:14px;align-items:center}
.call small{display:block;font-size:16px;color:#777}
.call strong{display:block;font-size:28px;color:var(--orange);font-weight:600;line-height:1.1}
.brand{position:absolute;left:50%;transform:translateX(-50%);top:22px;text-align:center}
.brand-name{font-family:"Raleway",sans-serif;font-weight:400;font-size:46px;color:var(--orange);line-height:1}
.brand-tag{font-size:14px;letter-spacing:3px;color:#777;margin-top:6px}
.masthead .btn{position:absolute;right:0;top:30px;height:56px}
.masthead .btn i{height:56px}

/* nav */
.mainnav{height:63px;background:var(--orange)}
.mainnav ul{list-style:none;display:flex;height:63px;align-items:center}
.mainnav li{font-family:"Raleway",sans-serif;font-weight:600;font-size:16px;color:#fff;padding:0 12px;height:63px;line-height:63px}
.mainnav li.active{background:var(--grey)}

/* hero */
.hero{height:511px;background:linear-gradient(100deg,#efe4cf 0%,#e7d6b6 45%,#dcc69f 100%)}
.hero-sketch{position:absolute;left:80px;top:220px;width:420px;height:290px;background:radial-gradient(ellipse at center,rgba(160,130,90,.28),rgba(160,130,90,0) 70%)}
.hero-portrait{position:absolute;left:710px;top:0;width:420px;height:511px;background:linear-gradient(180deg,#c9b08a 0%,#b7483f 55%,#c3332f 100%)}
.hero-copy{position:absolute;left:79px;top:60px}
.hero-kicker{font-family:"Merriweather",serif;font-style:italic;font-size:34px;color:#3a3a3a}
.hero-title{font-family:"Oswald",sans-serif;font-weight:500;font-size:72px;color:var(--orange);line-height:1.05;margin-top:6px}
.hero-sub{font-family:"Oswald",sans-serif;font-size:34px;color:#222;letter-spacing:1px;margin-top:6px}
.slide-arrow{position:absolute;top:236px;width:40px;height:36px;background:var(--orange);display:flex;align-items:center;justify-content:center}

/* welcome */
.welcome{height:310px;background:var(--orange);color:#fff;text-align:center;padding-top:50px}
.welcome h2{font-family:"Raleway",sans-serif;font-weight:400;font-size:40px}
.welcome .role{font-size:17px;margin-top:4px}
.welcome p{width:960px;margin:20px auto 0;font-size:13.5px;line-height:1.75}

/* skills */
.skills{height:498px;padding-top:60px}
.skill-row{display:flex;justify-content:space-between;margin-top:36px}
.skill{width:150px;text-align:center}
.skill h3{font-family:"Raleway",sans-serif;font-weight:500;font-size:17px;color:#666;margin-top:14px;line-height:1.25;min-height:44px}
.skill.active h3{color:var(--orange)}
.skill p{font-size:13px;line-height:1.6;color:#777;margin-top:8px}
.skill .chev{margin-top:8px}

/* experience / education */
.split{height:560px;display:flex}
.exp{width:600px;background:linear-gradient(135deg,#8e8e8e,#7a7a7a);padding:48px 0 0 79px}
.edu{width:600px;background:linear-gradient(135deg,#f2ac1c,#eea20a);padding:48px 80px 0 25px;color:#fff}
.split h2{font-family:"Raleway",sans-serif;font-weight:400;font-size:34px;letter-spacing:1px}
.exp h2{color:var(--orange)}
.acc{width:496px;margin-top:18px}
.acc-item{height:50px;background:#fff;border-radius:3px;margin-top:12px;display:flex;align-items:center;padding:0 18px;font-size:19px;color:#555;gap:14px;position:relative}
.acc-item.open{background:transparent;border:1px solid rgba(255,255,255,.35);color:var(--orange)}
.acc-item em{position:absolute;right:16px;font-style:normal;color:#888;font-size:16px}
.acc-body{color:#fff;font-size:13px;line-height:1.6;padding:14px 4px 4px}
.split .btn{margin-top:30px}
.edu .intro{font-size:13px;line-height:1.65;margin-top:16px}
.edu-item{display:flex;gap:26px;margin-top:22px}
.edu-item b{font-family:"Raleway",sans-serif;font-weight:300;font-size:50px;line-height:1}
.edu-item p{font-size:13px;line-height:1.6;padding-top:2px}

/* blog */
.blog{height:558px;background:var(--cream);padding-top:60px}
.posts{display:flex;justify-content:space-between;margin-top:36px}
.post{width:254px}
.post-img{height:178px}
.post h3{font-family:"Raleway",sans-serif;font-weight:700;font-size:17px;color:#333;margin-top:14px}
.post .date{color:var(--orange);font-size:13px;margin-top:6px;display:flex;gap:6px;align-items:center}
.post p{font-size:13px;line-height:1.6;color:#666;margin-top:8px}

/* employment + contact */
.work{height:540px;padding-top:60px}
.col-l{position:absolute;left:0;top:0;width:490px}
.col-r{position:absolute;left:545px;top:0;width:500px}
.divider{position:absolute;left:505px;top:-20px;width:1px;height:460px;background:#e2e2e2}
.work h2{font-family:"Raleway",sans-serif;font-weight:400;font-size:36px;color:var(--orange)}
.job{display:flex;gap:16px;margin-top:24px}
.years{width:86px;flex:none}
.years div{height:40px;color:#fff;font-size:19px;display:flex;align-items:center;justify-content:center}
.years .from{background:var(--orange)}
.years .to{background:var(--grey-dark)}
.job h3{font-size:17px;font-weight:600;color:#333}
.job p{font-size:13px;line-height:1.6;color:#777;margin-top:4px}
.col-l .btn{margin-top:26px}
.col-r .lead{font-size:15px;color:#555;margin-top:18px}
.field{border:1px solid #ccc;height:44px;margin-top:10px;font-size:13px;color:#555;padding:12px 10px}
.field.msg{height:138px}
.col-r .btn{margin-top:22px}

/* sites */
.sites{height:355px;background:var(--cream);padding-top:62px;text-align:center}
.sites p{width:760px;margin:16px auto 0;font-size:14px;line-height:1.6;color:#555}
.site-logos{display:flex;justify-content:space-between;align-items:center;margin-top:40px;padding:0 20px}
.site-name{font-family:"Raleway",sans-serif;font-weight:600;font-size:24px;color:#333;display:flex;align-items:center;gap:10px}
.site-name i{width:16px;height:16px;background:var(--orange);display:block}

/* footer */
.footer{height:353px;background:var(--orange);color:#fff;padding-top:40px}
.fcols{display:flex;justify-content:space-between}
.fcol{width:240px}
.fcol h4{font-family:"Raleway",sans-serif;font-weight:500;font-size:20px;margin-bottom:16px}
.fcol ul{list-style:none;font-size:14px;line-height:1.75}
.quote{font-size:13px;line-height:1.6}
.client{margin-top:12px;font-size:14px;font-weight:600}
.ci{display:flex;gap:10px;font-size:13px;line-height:1.5;margin-bottom:12px}
.fsocial{display:flex;gap:8px;margin-top:8px}
.fsocial b{width:34px;height:34px;border-radius:50%;background:#fff;display:block}
.map{height:170px;background:linear-gradient(135deg,#eef0ea,#dfe3d8);border:4px solid #fff}
.legal{height:41px;background:var(--grey);color:#fff;text-align:center;font-size:13px;line-height:41px}
.legal b{color:var(--orange)}
</style>
</head>
<body>

<div class="topbar"><div class="wrap">
  <div class="social" aria-label="Social links"><b></b><b></b><b></b></div>
  <div class="top-contact">
    <span><svg width="14" height="14" viewBox="0 0 24 24"><path fill="#f0a30a" d="M6.6 10.8a15 15 0 006.6 6.6l2.2-2.2c.3-.3.7-.4 1-.2 1.1.4 2.3.6 3.6.6.6 0 1 .4 1 1V20c0 .6-.4 1-1 1A17 17 0 013 4c0-.6.4-1 1-1h3.5c.6 0 1 .4 1 1 0 1.3.2 2.5.6 3.6.1.3 0 .7-.2 1z"/></svg>07 3000 0142</span>
    <span><svg width="16" height="12" viewBox="0 0 16 12"><rect x=".5" y=".5" width="15" height="11" fill="none" stroke="#f0a30a"/><path d="M1 1l7 6 7-6" fill="none" stroke="#f0a30a"/></svg>info@drmeganholt.com</span>
  </div>
</div></div>

<header class="masthead"><div class="wrap">
  <div class="call">
    <svg width="40" height="40" viewBox="0 0 24 24"><path fill="#f0a30a" d="M6.6 10.8a15 15 0 006.6 6.6l2.2-2.2c.3-.3.7-.4 1-.2 1.1.4 2.3.6 3.6.6.6 0 1 .4 1 1V20c0 .6-.4 1-1 1A17 17 0 013 4c0-.6.4-1 1-1h3.5c.6 0 1 .4 1 1 0 1.3.2 2.5.6 3.6.1.3 0 .7-.2 1z"/></svg>
    <div><small>Call Us Now</small><strong>07 3000 0142</strong></div>
  </div>
  <div class="brand"><div class="brand-name">Dr Megan Holt</div><div class="brand-tag">CHIROPRACTOR</div></div>
  <a class="btn"><span>BOOK APPOINTMENT</span><i><svg width="12" height="20" viewBox="0 0 12 20"><path d="M2 2l8 8-8 8" stroke="#fff" stroke-width="2" fill="none"/></svg></i></a>
</div></header>

<nav class="mainnav"><div class="wrap"><ul>
  <li class="active">HOME</li><li>ABOUT ME</li><li>SKILLS</li><li>PROFESSIONAL EXPERIENCES</li><li>EDUCATION</li><li>EMPLOYMENT</li><li>MY SITES</li><li>BLOG</li><li>CONTACT</li>
</ul></div></nav>

<section class="hero">
  <div class="hero-sketch" role="img" aria-label="Faint anatomical spine sketch on parchment texture"></div>
  <div class="hero-portrait" role="img" aria-label="Portrait of Dr Megan Holt in a red jacket"></div>
  <div class="hero-copy">
    <div class="hero-kicker">Personal Attention</div>
    <div class="hero-title">I AM DR MEGAN HOLT</div>
    <div class="hero-sub">BSC MCHIRO DIBAK</div>
  </div>
  <div class="slide-arrow" style="left:0"><svg width="10" height="14" viewBox="0 0 10 14"><path d="M8 1L2 7l6 6" stroke="#fff" stroke-width="2" fill="none"/></svg></div>
  <div class="slide-arrow" style="right:0"><svg width="10" height="14" viewBox="0 0 10 14"><path d="M2 1l6 6-6 6" stroke="#fff" stroke-width="2" fill="none"/></svg></div>
</section>

<section class="welcome">
  <h2>WELCOME TO DR MEGAN HOLT</h2>
  <div class="role">chiropractor</div>
  <p>Hello, I am a Chiropractor and a Diplomate of the Global Academy of Applied Kinesiology (GAAK). I am also on the board of certified teachers for the GAAK. Teaching engagements take me to local, national and international destinations. Thank you for visiting my page. I look forward to sharing some of my insights with you via my blog. I am born and bred here in Brisbane, Australia and love this city that I call home.</p>
  <svg style="margin-top:10px" width="20" height="18" viewBox="0 0 20 18"><path d="M3 2l7 6 7-6M3 9l7 6 7-6" stroke="#fff" stroke-width="2" fill="none"/></svg>
</section>

<section class="skills"><div class="wrap">
  <h2 class="h-section">OUR SKILL</h2>
  <div class="skill-row">
    <div class="skill active">
      <svg width="120" height="120" viewBox="0 0 120 120"><circle cx="60" cy="60" r="54" fill="#f0a30a"/><circle cx="60" cy="64" r="50" fill="#fff"/><rect x="38" y="44" width="44" height="30" fill="none" stroke="#f0a30a" stroke-width="3"/><path d="M44 66l10-10 8 6 12-12M60 74v10M52 86h16" stroke="#f0a30a" stroke-width="3" fill="none"/></svg>
      <h3>BUSINESS DEVELOPMENT</h3><p>I founded an award winning Chiropractic healthcare clinic.</p>
      <svg class="chev" width="16" height="14" viewBox="0 0 20 18"><path d="M3 2l7 6 7-6M3 9l7 6 7-6" stroke="#f0a30a" stroke-width="2" fill="none"/></svg>
    </div>
    <div class="skill">
      <svg width="120" height="120" viewBox="0 0 120 120"><circle cx="60" cy="60" r="54" fill="#7c7c7c"/><circle cx="60" cy="64" r="50" fill="#fff"/><path d="M36 54h12l26-14v40L48 66H36z M44 66l4 16h8l-4-16" stroke="#7c7c7c" stroke-width="3" fill="none"/><path d="M80 52h8M80 60h10M80 68h8" stroke="#7c7c7c" stroke-width="3"/></svg>
      <h3>TEACHING</h3><p>I love the symbiotic relationship I have with my students.</p>
      <svg class="chev" width="16" height="14" viewBox="0 0 20 18"><path d="M3 2l7 6 7-6M3 9l7 6 7-6" stroke="#f0a30a" stroke-width="2" fill="none"/></svg>
    </div>
    <div class="skill">
      <svg width="120" height="120" viewBox="0 0 120 120"><circle cx="60" cy="60" r="54" fill="#7c7c7c"/><circle cx="60" cy="64" r="50" fill="#fff"/><circle cx="58" cy="64" r="22" fill="none" stroke="#7c7c7c" stroke-width="3"/><circle cx="58" cy="64" r="13" fill="none" stroke="#7c7c7c" stroke-width="3"/><circle cx="58" cy="64" r="4" fill="#f0a30a"/><path d="M58 64l26-22M78 42h8v-8" stroke="#f0a30a" stroke-width="3" fill="none"/></svg>
      <h3>CHIROPRACTIC SKILLS</h3><p>Diagnostics using functional neurology and manual muscle.</p>
      <svg class="chev" width="16" height="14" viewBox="0 0 20 18"><path d="M3 2l7 6 7-6M3 9l7 6 7-6" stroke="#f0a30a" stroke-width="2" fill="none"/></svg>
    </div>
    <div class="skill">
      <svg width="120" height="120" viewBox="0 0 120 120"><circle cx="60" cy="60" r="54" fill="#7c7c7c"/><circle cx="60" cy="64" r="50" fill="#fff"/><path d="M60 84L40 64a12 12 0 0120-14 12 12 0 0120 14z" fill="none" stroke="#f0a30a" stroke-width="3"/></svg>
      <h3>MOTHER AND WIFE</h3><p>I am a wife of a widower (WOM), a mother of two - one was a bonus.</p>
      <svg class="chev" width="16" height="14" viewBox="0 0 20 18"><path d="M3 2l7 6 7-6M3 9l7 6 7-6" stroke="#f0a30a" stroke-width="2" fill="none"/></svg>
    </div>
    <div class="skill">
      <svg width="120" height="120" viewBox="0 0 120 120"><circle cx="60" cy="60" r="54" fill="#7c7c7c"/><circle cx="60" cy="64" r="50" fill="#fff"/><path d="M38 80l14-16 12 8 18-24" stroke="#f0a30a" stroke-width="3" fill="none"/><circle cx="38" cy="80" r="4" fill="#7c7c7c"/><circle cx="52" cy="64" r="4" fill="#7c7c7c"/><circle cx="64" cy="72" r="4" fill="#7c7c7c"/><circle cx="82" cy="48" r="4" fill="#7c7c7c"/></svg>
      <h3>PRODUCT LAUNCHING</h3><p>I have a special interest in product launching using the power.</p>
      <svg class="chev" width="16" height="14" viewBox="0 0 20 18"><path d="M3 2l7 6 7-6M3 9l7 6 7-6" stroke="#f0a30a" stroke-width="2" fill="none"/></svg>
    </div>
    <div class="skill">
      <svg width="120" height="120" viewBox="0 0 120 120"><circle cx="60" cy="60" r="54" fill="#7c7c7c"/><circle cx="60" cy="64" r="50" fill="#fff"/><path d="M46 42h28l-2 18a12 12 0 01-24 0z M60 72v14M50 86h20" stroke="#7c7c7c" stroke-width="3" fill="none"/><path d="M48 54h24" stroke="#f0a30a" stroke-width="3"/></svg>
      <h3>EVENT CO-ORDINATION</h3><p>There's nothing quite like a deadline to get you focussed.</p>
      <svg class="chev" width="16" height="14" viewBox="0 0 20 18"><path d="M3 2l7 6 7-6M3 9l7 6 7-6" stroke="#f0a30a" stroke-width="2" fill="none"/></svg>
    </div>
  </div>
</div></section>

<section class="split">
  <div class="exp">
    <h2>PROFESSIONAL EXPERIENCES</h2>
    <div class="acc">
      <div class="acc-item open"><svg width="18" height="18" viewBox="0 0 18 18"><path d="M7 11l4-4M6 8L4 10a3 3 0 004 4l2-2M12 10l2-2a3 3 0 00-4-4L8 6" stroke="#f0a30a" stroke-width="1.6" fill="none"/></svg>2017<em>–</em></div>
      <div class="acc-body">Started KinetiqOZ – Exclusive Distributors for Vitalgel Queensland, New South Wales and Victoria. KinetiqOZ is sponsoring 'Everybody is an Athlete' for the GAAK A in Adelaide in April.</div>
      <div class="acc-item"><svg width="18" height="18" viewBox="0 0 18 18"><path d="M7 11l4-4M6 8L4 10a3 3 0 004 4l2-2M12 10l2-2a3 3 0 00-4-4L8 6" stroke="#777" stroke-width="1.6" fill="none"/></svg>2016<em>+</em></div>
      <div class="acc-item"><svg width="18" height="18" viewBox="0 0 18 18"><path d="M7 11l4-4M6 8L4 10a3 3 0 004 4l2-2M12 10l2-2a3 3 0 00-4-4L8 6" stroke="#777" stroke-width="1.6" fill="none"/></svg>2015<em>+</em></div>
      <div class="acc-item"><svg width="18" height="18" viewBox="0 0 18 18"><path d="M7 11l4-4M6 8L4 10a3 3 0 004 4l2-2M12 10l2-2a3 3 0 00-4-4L8 6" stroke="#777" stroke-width="1.6" fill="none"/></svg>2014<em>+</em></div>
    </div>
    <a class="btn"><span>VIEW ALL</span><i><svg width="12" height="20" viewBox="0 0 12 20"><path d="M2 2l8 8-8 8" stroke="#fff" stroke-width="2" fill="none"/></svg></i></a>
  </div>
  <div class="edu">
    <h2>EDUCATION</h2>
    <p class="intro">Life is for learning. &nbsp;The more I learn, the more curious I become. I have a thirst to understand things &amp; passionately inquisitive. My patients &amp; my children are my greatest teachers. But here are my formal foundation studies.</p>
    <div class="edu-item"><b>01</b><p>Global Academy of Applied Kinesiology Diplomate of the Global Board of Applied Kinesiology Board of Certified Teachers ANTWERP, BELGIUM 2008</p></div>
    <div class="edu-item"><b>02</b><p>Harbour City University Master of Chiropractic<br>SYDNEY, AUSTRALIA 2000-2002</p></div>
    <div class="edu-item"><b>03</b><p>Northern Coast University Bachelor of Science (Anatomy)<br>BRISBANE, AUSTRALIA 1997-1999</p></div>
    <a class="btn" style="margin-left:0"><span>VIEW ALL</span><i><svg width="12" height="20" viewBox="0 0 12 20"><path d="M2 2l8 8-8 8" stroke="#fff" stroke-width="2" fill="none"/></svg></i></a>
  </div>
</section>

<section class="blog"><div class="wrap">
  <h2 class="h-section">LATEST BLOG</h2>
  <div class="posts">
    <article class="post"><div class="post-img" role="img" aria-label="Chiropractor treating a patient's back" style="background:linear-gradient(135deg,#efe9e2,#cdb7a3)"></div><h3>LOREM IPSUM TEXT</h3><div class="date"><svg width="12" height="12" viewBox="0 0 12 12"><rect x="1" y="2" width="10" height="9" fill="none" stroke="#f0a30a"/><path d="M1 5h10" stroke="#f0a30a"/></svg>26 April 2016</div><p>Lorem Ipsum is simply dummy text of the printing &amp; typesetting industry. Lorem Ipsum has.</p></article>
    <article class="post"><div class="post-img" role="img" aria-label="Close-up model of a spine" style="background:linear-gradient(135deg,#f4efe6,#d8c3a0)"></div><h3>LOREM IPSUM TEXT</h3><div class="date"><svg width="12" height="12" viewBox="0 0 12 12"><rect x="1" y="2" width="10" height="9" fill="none" stroke="#f0a30a"/><path d="M1 5h10" stroke="#f0a30a"/></svg>26 April 2016</div><p>Lorem Ipsum is simply dummy text of the printing &amp; typesetting industry. Lorem Ipsum has.</p></article>
    <article class="post"><div class="post-img" role="img" aria-label="Doctors reviewing an x-ray" style="background:linear-gradient(135deg,#e9eef2,#b9c7d2)"></div><h3>LOREM IPSUM TEXT</h3><div class="date"><svg width="12" height="12" viewBox="0 0 12 12"><rect x="1" y="2" width="10" height="9" fill="none" stroke="#f0a30a"/><path d="M1 5h10" stroke="#f0a30a"/></svg>26 April 2016</div><p>Lorem Ipsum is simply dummy text of the printing &amp; typesetting industry. Lorem Ipsum has.</p></article>
    <article class="post"><div class="post-img" role="img" aria-label="Back view of a man with highlighted spine" style="background:linear-gradient(135deg,#fbfbfb,#d9a37c)"></div><h3>LOREM IPSUM TEXT</h3><div class="date"><svg width="12" height="12" viewBox="0 0 12 12"><rect x="1" y="2" width="10" height="9" fill="none" stroke="#f0a30a"/><path d="M1 5h10" stroke="#f0a30a"/></svg>26 April 2016</div><p>Lorem Ipsum is simply dummy text of the printing &amp; typesetting industry. Lorem Ipsum has.</p></article>
  </div>
</div></section>

<section class="work"><div class="wrap">
  <div class="col-l">
    <h2>EMPLOYMENT</h2>
    <div class="job"><div class="years"><div class="from">2005 -</div><div class="to">2017</div></div><div><h3>Well Aligned Studio Founder, Chiropractor</h3><p>What a wonderful place to work! I can't come to this clinic and not feel happy. It's decorated...</p></div></div>
    <div class="job"><div class="years"><div class="from">2004 -</div><div class="to">2005</div></div><div><h3>Harbourside Spine &amp; Health</h3><p>I learned a lot from my mentor Dr Paul Ashcombe here. He taught me how to think like a...</p></div></div>
    <div class="job"><div class="years"><div class="from">2003 -</div><div class="to">2004</div></div><div><h3>Coastal Balance Centre Associate</h3><p>Working under Dr Gordon Lyle has been the greatest gift I could have imagined first year out...</p></div></div>
    <a class="btn"><span>VIEW ALL</span><i><svg width="12" height="20" viewBox="0 0 12 20"><path d="M2 2l8 8-8 8" stroke="#fff" stroke-width="2" fill="none"/></svg></i></a>
  </div>
  <div class="divider"></div>
  <div class="col-r">
    <h2>CONTACT US</h2>
    <p class="lead">Need a free quote, or have a question? Get in touch!</p>
    <div class="field">Name*</div>
    <div class="field">Email*</div>
    <div class="field">Phone*</div>
    <div class="field msg">Message*</div>
    <a class="btn"><span>SUBMIT</span><i><svg width="12" height="20" viewBox="0 0 12 20"><path d="M2 2l8 8-8 8" stroke="#fff" stroke-width="2" fill="none"/></svg></i></a>
  </div>
</div></section>

<section class="sites"><div class="wrap">
  <h2 class="h-section">MY SITES</h2>
  <p>Lorem Ipsum is simply dummy text of the printing and typesetting industry. Lorem Ipsum has been. Lorem Ipsum is simply dummy text of the printing and typesetting industry.</p>
  <div class="site-logos">
    <div class="site-name"><i></i>Dr Megan's Blog</div>
    <div class="site-name"><i></i>KinetiqOZ</div>
    <div class="site-name"><i></i>learnmotion.com.au</div>
    <div class="site-name"><i></i>Restored Reflex</div>
  </div>
</div></section>

<footer class="footer"><div class="wrap">
  <div class="fcols">
    <div class="fcol"><h4>SiteMap</h4><ul><li>» Home</li><li>» About Me</li><li>» Skills</li><li>» Professional Experiences</li><li>» Education</li><li>» Employment</li><li>» My Sites</li><li>» Blog</li><li>» Contact</li></ul></div>
    <div class="fcol"><h4>Testimonials</h4><p class="quote">“ Lorem Ipsum is simply dummy text of the printing and typesetting of industry. Lorem Ipsum has been the industry's standard. ”</p><div class="client">— CLIENT NAME</div><div style="margin-top:14px;font-size:18px">‹ ›</div></div>
    <div class="fcol"><h4>Get In Touch</h4>
      <div class="ci"><svg width="14" height="14" viewBox="0 0 14 14"><path d="M7 1v12M2 4h10M3 8h8" stroke="#fff" stroke-width="1.5"/></svg><div><b>DR MEGAN HOLT</b><br>101 - Lorem Ipsum is simple text of print and type setting.</div></div>
      <div class="ci"><svg width="14" height="14" viewBox="0 0 24 24"><path fill="#fff" d="M6.6 10.8a15 15 0 006.6 6.6l2.2-2.2c.3-.3.7-.4 1-.2 1.1.4 2.3.6 3.6.6.6 0 1 .4 1 1V20c0 .6-.4 1-1 1A17 17 0 013 4c0-.6.4-1 1-1h3.5c.6 0 1 .4 1 1 0 1.3.2 2.5.6 3.6.1.3 0 .7-.2 1z"/></svg>07 3000 0142</div>
      <div class="ci"><svg width="16" height="12" viewBox="0 0 16 12"><rect x=".5" y=".5" width="15" height="11" fill="none" stroke="#fff"/><path d="M1 1l7 6 7-6" fill="none" stroke="#fff"/></svg>info@drmeganholt.com</div>
      <div class="fsocial"><b></b><b></b><b></b></div>
    </div>
    <div class="fcol"><h4>Location Map</h4><div class="map" role="img" aria-label="Street map showing the clinic location"></div></div>
  </div>
</div></footer>

<div class="legal">© 2017 <b>DR MEGAN HOLT</b> - All Right Reserved</div>

</body>
</html>
```